Business Card Design

We need a business card design for a new company based in Allen, Texas. (outside of Dallas,Texas) We offer Business Management Solutions to Entrepreneurs, as well as Corporate Businesses. Our product line offers solutions to Image, Branding, Social Media marketing, business development strategies, banking / funding solutions, just to name a few. We would like to see designs that convey strength and confidence. I have attached a sample design of our company name. Designers you may use company name as either: Tovan or Tovan Corporation, depending on the design layout.

Please show alternate color of Black as well.

Industry/Entity Type

Business

Contact Information for Business Card

Tovan Corporation

4862 N. Brisbury Lane, STE 300
Halden, TX 76240
Office: 512.638.4471
Fax: 512.638.4472

Dr. Louis Brennick
Business Development Director

```html
<!DOCTYPE html>
<html lang="en">
<head>
<meta charset="utf-8">
<title>Tovan Corporation – Business Card</title>
<link href="https://fonts.googleapis.com/css2?family=Open+Sans:wght@300;400;600&display=swap" rel="stylesheet">
<style>
  :root {
    --page: #ececec;
    --card-white: #ffffff;
    --card-black: #1d1d1d;
    --band-light: #f1f1f1;
    --mark-grey: #d6d6d6;
    --text-dark: #1a1a1a;
    --text-mid: #444444;
    --text-soft: #c4c4c4;
    --logo-grey: #d8d8d8;
  }
  * { margin: 0; padding: 0; box-sizing: border-box; }
  html, body { width: 1200px; height: 1200px; overflow: hidden; }
  body {
    background: var(--page);
    font-family: "Open Sans", Arial, sans-serif;
    position: relative;
  }
  .card {
    position: absolute;
    left: 250px;
    width: 700px;
    height: 400px;
    box-shadow: 0 6px 18px rgba(0,0,0,0.12);
    overflow: hidden;
  }
  /* Front */
  .card-front { top: 150px; background: var(--card-white); }
  .front-band {
    position: absolute;
    left: 120px; top: 110px;
    width: 460px; height: 110px;
    background: var(--card-black);
    display: flex; align-items: center; justify-content: flex-end;
    padding-right: 34px;
  }
  .front-wordmark {
    font-weight: 300;
    font-size: 40px;
    color: var(--logo-grey);
    letter-spacing: 0.5px;
    white-space: nowrap;
  }
  /* Back */
  .card-back { top: 650px; background: var(--card-black); }
  .back-square {
    position: absolute;
    left: 40px; top: 78px;
    width: 46px; height: 46px;
    background: var(--mark-grey);
  }
  .back-wordmark {
    position: absolute;
    left: 106px; top: 62px;
    font-weight: 300;
    font-size: 64px;
    line-height: 1;
    color: var(--card-white);
  }
  .name-band {
    position: absolute;
    left: 320px; top: 152px;
    width: 380px; height: 74px;
    background: var(--band-light);
    padding: 10px 22px;
  }
  .person-name { font-weight: 600; font-size: 24px; line-height: 1.2; color: var(--text-dark); white-space: nowrap; }
  .person-title { font-weight: 400; font-size: 18px; line-height: 1.3; color: var(--text-mid); white-space: nowrap; }
  .contact {
    position: absolute;
    left: 330px; top: 240px;
    color: var(--text-soft);
    font-size: 17px;
    line-height: 25px;
    white-space: nowrap;
  }
  .contact-line { display: flex; align-items: center; gap: 10px; }
  .contact-icon { width: 16px; height: 16px; flex: none; }
</style>
</head>
<body>
  <section class="card card-front" aria-label="Business card front">
    <div class="front-band">
      <span class="front-wordmark">Tovan Corporation</span>
    </div>
  </section>

  <section class="card card-back" aria-label="Business card back">
    <div class="back-square"></div>
    <div class="back-wordmark">Tovan</div>
    <div class="name-band">
      <p class="person-name">Dr. Louis Brennick</p>
      <p class="person-title">Business Development Director</p>
    </div>
    <div class="contact">
      <p>Tovan Corporation 4862</p>
      <p>N. Brisbury Lane,</p>
      <p>STE 300 Halden, TX 76240</p>
      <p class="contact-line">
        <svg class="contact-icon" viewBox="0 0 16 16" aria-hidden="true">
          <rect x="0" y="0" width="16" height="16" rx="2" fill="#c4c4c4"/>
          <path d="M5 3.5 L7 5.5 L6 7 Q7 9 9 10 L10.5 9 L12.5 11 L11 12.5 Q7 12.5 3.5 5 Z" fill="#1d1d1d"/>
        </svg>
        512.638.4471
      </p>
      <p class="contact-line">
        <svg class="contact-icon" viewBox="0 0 16 16" aria-hidden="true">
          <rect x="0" y="0" width="16" height="16" rx="2" fill="#c4c4c4"/>
          <rect x="3" y="6" width="10" height="6" fill="#1d1d1d"/>
          <rect x="5" y="3" width="6" height="4" fill="#1d1d1d"/>
          <rect x="5" y="9" width="6" height="1" fill="#c4c4c4"/>
        </svg>
        512.638.4472
      </p>
    </div>
  </section>
</body>
</html>
```